Menu Design Project

This is a sushi menu. We need to polish the menu. You can re-size logo and add color and graphic to make inviting. Please feel free to make any recommendations.

Upscale crowd

```html
<!DOCTYPE html>
<html lang="en">
<head>
<meta charset="utf-8">
<title>Kazeno Sushi Bar — Menu</title>
<link rel="stylesheet" href="https://fonts.googleapis.com/css2?family=Josefin+Sans:wght@400;600&family=Questrial&display=swap">
<style>
  :root {
    --stage: #2a2a2a;
    --sheet: #5b5b5d;
    --sheet-dark: #3d3d3f;
    --sheet-panel: #6a6a6c;
    --red: #d21f26;
    --ink: #f1f1f1;
    --ink-soft: #c9c9c9;
    --black: #0d0d0d;
  }
  * { box-sizing: border-box; margin: 0; padding: 0; }
  html, body { width: 1200px; height: 850px; overflow: hidden; }
  body {
    background: var(--stage);
    font-family: "Questrial", sans-serif;
    color: var(--ink);
    position: relative;
  }
  ul { list-style: none; }

  .menu-sheet {
    position: absolute;
    width: 740px;
    height: 410px;
    background: var(--sheet);
    box-shadow: 0 6px 18px rgba(0,0,0,.55);
    overflow: hidden;
  }
  .menu-sheet--front { left: 20px; top: 20px; }
  .menu-sheet--back { left: 440px; top: 420px; }

  .sheet-pattern {
    position: absolute; inset: 0;
    background:
      radial-gradient(ellipse 180px 140px at 70% 45%, rgba(255,255,255,.07), transparent 70%),
      radial-gradient(ellipse 160px 120px at 30% 65%, rgba(255,255,255,.05), transparent 70%);
  }
  .top-band { position: absolute; left: 0; right: 0; top: 0; height: 5px; background: var(--red); }
  .bottom-band {
    position: absolute; left: 0; right: 0; bottom: 0; height: 22px;
    background: var(--red);
    display: flex; flex-direction: column; justify-content: center; align-items: center;
    font-size: 5.5px; line-height: 7px; color: var(--ink);
  }

  .sheet-columns {
    position: absolute; left: 0; right: 0; top: 5px; bottom: 22px;
    display: grid; grid-template-columns: 250px 1fr 1fr;
  }
  .menu-col { padding: 8px 12px; position: relative; }
  .menu-col--dark { background: var(--sheet-dark); }

  .section-title {
    font-family: "Josefin Sans", sans-serif;
    font-weight: 400;
    font-size: 10px;
    letter-spacing: 4px;
    text-align: center;
    color: var(--ink);
    margin: 5px 0 3px;
  }
  .item {
    display: flex; gap: 3px;
    font-size: 6px; line-height: 8.6px;
    color: var(--ink-soft);
  }
  .item-name { color: var(--ink); font-weight: 700; white-space: nowrap; }
  .item-desc { flex: 1; white-space: nowrap; overflow: hidden; }
  .price { width: 14px; text-align: right; color: var(--ink); }

  .brand-block {
    position: absolute; top: -5px; left: 14px;
    width: 96px; height: 84px;
    background: var(--black);
    display: flex; flex-direction: column; align-items: center; justify-content: center; gap: 5px;
  }
  .brand-dot { width: 30px; height: 30px; border-radius: 50%; background: var(--red); }
  .brand-name {
    font-family: "Josefin Sans", sans-serif; font-weight: 600;
    font-size: 9.5px; letter-spacing: 1px; text-align: center; line-height: 11px;
    color: var(--ink); text-transform: uppercase;
  }
  .brand-offset { margin-top: 86px; }

  .specials {
    background: var(--sheet-panel);
    border-top: 3px solid var(--red);
    padding: 2px 8px 6px;
    margin-top: 4px;
  }
  .note { font-size: 6px; color: var(--ink-soft); margin-top: 4px; }

  .fish-grid {
    display: grid; grid-template-columns: repeat(3, 1fr); column-gap: 6px;
  }
  .fish-grid .item { font-size: 5.6px; }

  .brand-block--small {
    position: absolute; right: 12px; bottom: 28px;
    width: 52px; height: 46px; top: auto; left: auto; gap: 3px;
  }
  .brand-block--small .brand-dot { width: 16px; height: 16px; }
  .brand-block--small .brand-name { font-size: 5.5px; line-height: 6.5px; letter-spacing: .5px; }
</style>
</head>
<body>

<!-- Front side -->
<section class="menu-sheet menu-sheet--front" aria-label="Menu front">
  <div class="sheet-pattern" role="img" aria-label="Faint koi and wave pattern"></div>
  <div class="top-band"></div>
  <div class="sheet-columns">
    <div class="menu-col menu-col--dark">
      <h2 class="section-title">appetizers</h2>
      <ul>
        <li class="item"><span class="item-name">edamame</span><span class="item-desc">steamed salted soy beans</span><span class="price">5</span></li>
        <li class="item"><span class="item-name">gyoza</span><span class="item-desc">pan fried pork dumplings</span><span class="price">7</span></li>
        <li class="item"><span class="item-name">agedashi tofu</span><span class="item-desc">crisp tofu in dashi</span><span class="price">7</span></li>
        <li class="item"><span class="item-name">shishito peppers</span><span class="item-desc">blistered with sea salt</span><span class="price">8</span></li>
        <li class="item"><span class="item-name">tuna tataki</span><span class="item-desc">seared tuna, ponzu</span><span class="price">13</span></li>
        <li class="item"><span class="item-name">yellowtail crudo</span><span class="item-desc">jalapeño and yuzu</span><span class="price">14</span></li>
        <li class="item"><span class="item-name">soft shell crab</span><span class="item-desc">tempura with ponzu</span><span class="price">12</span></li>
        <li class="item"><span class="item-name">beef negimaki</span><span class="item-desc">scallion rolled in beef</span><span class="price">11</span></li>
        <li class="item"><span class="item-name">chicken karaage</span><span class="item-desc">ginger fried chicken</span><span class="price">9</span></li>
        <li class="item"><span class="item-name">squid salad</span><span class="item-desc">marinated with sesame</span><span class="price">8</span></li>
        <li class="item"><span class="item-name">takoyaki</span><span class="item-desc">octopus balls, bonito</span><span class="price">8</span></li>
        <li class="item"><span class="item-name">shrimp shumai</span><span class="item-desc">steamed with mustard</span><span class="price">7</span></li>
      </ul>
      <h2 class="section-title">soup</h2>
      <ul>
        <li class="item"><span class="item-name">miso soup</span><span class="item-desc">tofu, seaweed, scallion</span><span class="price">3</span></li>
        <li class="item"><span class="item-name">clear soup</span><span class="item-desc">mushroom and scallion</span><span class="price">3</span></li>
        <li class="item"><span class="item-name">seafood soup</span><span class="item-desc">shrimp, scallop, fish</span><span class="price">9</span></li>
      </ul>
      <h2 class="section-title">salads</h2>
      <ul>
        <li class="item"><span class="item-name">house salad</span><span class="item-desc">ginger dressing greens</span><span class="price">5</span></li>
        <li class="item"><span class="item-name">seaweed salad</span><span class="item-desc">sesame marinated wakame</span><span class="price">6</span></li>
        <li class="item"><span class="item-name">avocado salad</span><span class="item-desc">greens with citrus</span><span class="price">7</span></li>
        <li class="item"><span class="item-name">cucumber salad</span><span class="item-desc">rice vinegar dressing</span><span class="price">5</span></li>
        <li class="item"><span class="item-name">spicy tuna salad</span><span class="item-desc">mixed greens, tobiko</span><span class="price">12</span></li>
      </ul>
      <h2 class="section-title">noodles</h2>
      <ul>
        <li class="item"><span class="item-name">nabeyaki udon</span><span class="item-desc">shrimp tempura, egg</span><span class="price">14</span></li>
        <li class="item"><span class="item-name">tempura soba</span><span class="item-desc">buckwheat noodles, broth</span><span class="price">13</span></li>
        <li class="item"><span class="item-name">yaki udon</span><span class="item-desc">stir fried with vegetables</span><span class="price">12</span></li>
        <li class="item"><span class="item-name">zaru soba</span><span class="item-desc">chilled with dipping sauce</span><span class="price">10</span></li>
      </ul>
    </div>

    <div class="menu-col">
      <div class="brand-block">
        <div class="brand-dot"></div>
        <div class="brand-name">Kazeno<br>Sushi Bar</div>
      </div>
      <ul class="brand-offset">
        <li class="item"><span class="item-name">mixed tempura</span><span class="item-desc">shrimp and vegetables</span><span class="price">16</span></li>
        <li class="item"><span class="item-name">salmon teriyaki</span><span class="item-desc">grilled with glaze</span><span class="price">19</span></li>
        <li class="item"><span class="item-name">beef teriyaki</span><span class="item-desc">ribeye with sauce</span><span class="price">22</span></li>
        <li class="item"><span class="item-name">chicken katsu</span><span class="item-desc">panko fried cutlet</span><span class="price">15</span></li>
        <li class="item"><span class="item-name">una don</span><span class="item-desc">eel over rice</span><span class="price">21</span></li>
      </ul>
      <h2 class="section-title">entrées</h2>
      <ul>
        <li class="item"><span class="item-name">chirashi</span><span class="item-desc">assorted fish over rice</span><span class="price">24</span></li>
        <li class="item"><span class="item-name">sushi dinner</span><span class="item-desc">chef selected nigiri</span><span class="price">26</span></li>
        <li class="item"><span class="item-name">sashimi dinner</span><span class="item-desc">fifteen fresh pieces</span><span class="price">29</span></li>
        <li class="item"><span class="item-name">shrimp tempura</span><span class="item-desc">with dipping sauce</span><span class="price">18</span></li>
        <li class="item"><span class="item-name">chicken teriyaki</span><span class="item-desc">served with rice</span><span class="price">16</span></li>
        <li class="item"><span class="item-name">beef negimaki</span><span class="item-desc">scallion and sauce</span><span class="price">21</span></li>
        <li class="item"><span class="item-name">salmon shioyaki</span><span class="item-desc">salt grilled fillet</span><span class="price">20</span></li>
        <li class="item"><span class="item-name">tofu steak</span><span class="item-desc">grilled with miso</span><span class="price">14</span></li>
      </ul>
      <p class="note">all entrées served with miso soup</p>
    </div>

    <div class="menu-col">
      <ul>
        <li class="item"><span class="item-name">inari roll</span><span class="item-desc">sweet tofu, cucumber</span><span class="price">6</span></li>
        <li class="item"><span class="item-name">asparagus maki</span><span class="item-desc">tempura flakes, sauce</span><span class="price">6</span></li>
        <li class="item"><span class="item-name">futomaki</span><span class="item-desc">egg, squash, cucumber</span><span class="price">8</span></li>
        <li class="item"><span class="item-name">unagi roll</span><span class="item-desc">eel and avocado</span><span class="price">9</span></li>
      </ul>
      <h2 class="section-title">sides</h2>
      <ul>
        <li class="item"><span class="item-name">steamed rice</span><span class="item-desc"></span><span class="price">2</span></li>
        <li class="item"><span class="item-name">brown rice</span><span class="item-desc"></span><span class="price">3</span></li>
        <li class="item"><span class="item-name">sushi rice</span><span class="item-desc"></span><span class="price">3</span></li>
        <li class="item"><span class="item-name">miso soup</span><span class="item-desc"></span><span class="price">3</span></li>
        <li class="item"><span class="item-name">ginger dressing</span><span class="item-desc"></span><span class="price">1</span></li>
      </ul>
      <div class="specials">
        <h2 class="section-title">specials</h2>
        <ul>
          <li class="item"><span class="item-desc">chicken and shrimp teriyaki</span><span class="price">24</span></li>
          <li class="item"><span class="item-desc">salmon and tuna sashimi</span><span class="price">28</span></li>
          <li class="item"><span class="item-desc">shrimp and vegetable tempura</span><span class="price">19</span></li>
          <li class="item"><span class="item-desc">beef and chicken negimaki</span><span class="price">23</span></li>
          <li class="item"><span class="item-desc">lobster tempura roll</span><span class="price">18</span></li>
          <li class="item"><span class="item-desc">toro nigiri trio</span><span class="price">26</span></li>
          <li class="item"><span class="item-desc">wagyu tataki</span><span class="price">32</span></li>
          <li class="item"><span class="item-desc">yellowtail collar</span><span class="price">16</span></li>
          <li class="item"><span class="item-desc">black cod miso</span><span class="price">29</span></li>
          <li class="item"><span class="item-desc">king crab legs</span><span class="price">38</span></li>
          <li class="item"><span class="item-desc">scallop dynamite</span><span class="price">17</span></li>
          <li class="item"><span class="item-desc">omakase tasting</span><span class="price">85</span></li>
        </ul>
      </div>
    </div>
  </div>
  <footer class="bottom-band">
    <p>Please inform your server of any allergies before ordering.</p>
    <p>Consuming raw or undercooked fish may increase health risk.</p>
  </footer>
</section>

<!-- Back side -->
<section class="menu-sheet menu-sheet--back" aria-label="Menu back">
  <div class="sheet-pattern" role="img" aria-label="Faint koi and wave pattern"></div>
  <div class="top-band"></div>
  <div class="sheet-columns">
    <div class="menu-col menu-col--dark">
      <h2 class="section-title">drinks</h2>
      <ul>
        <li class="item"><span class="item-name">green tea</span><span class="item-desc"></span><span class="price">2</span></li>
        <li class="item"><span class="item-name">ramune soda</span><span class="item-desc"></span><span class="price">4</span></li>
        <li class="item"><span class="item-name">sparkling water</span><span class="item-desc"></span><span class="price">4</span></li>
        <li class="item"><span class="item-name">iced tea</span><span class="item-desc"></span><span class="price">3</span></li>
        <li class="item"><span class="item-name">fresh juice</span><span class="item-desc"></span><span class="price">4</span></li>
        <li class="item"><span class="item-name">cola</span><span class="item-desc"></span><span class="price">2</span></li>
      </ul>
      <h2 class="section-title">dessert</h2>
      <ul>
        <li class="item"><span class="item-name">mochi ice cream</span><span class="item-desc"></span><span class="price">6</span></li>
        <li class="item"><span class="item-name">green tea ice cream</span><span class="item-desc"></span><span class="price">5</span></li>
        <li class="item"><span class="item-name">tempura banana</span><span class="item-desc"></span><span class="price">7</span></li>
        <li class="item"><span class="item-name">red bean cake</span><span class="item-desc"></span><span class="price">6</span></li>
      </ul>
      <h2 class="section-title">signature rolls</h2>
      <ul>
        <li class="item"><span class="item-name">dragon roll</span><span class="item-desc">eel, avocado, cucumber</span><span class="price">15</span></li>
        <li class="item"><span class="item-name">rainbow roll</span><span class="item-desc">assorted fish over california</span><span class="price">15</span></li>
        <li class="item"><span class="item-name">volcano roll</span><span class="item-desc">baked scallop, spicy mayo</span><span class="price">16</span></li>
        <li class="item"><span class="item-name">spider roll</span><span class="item-desc">soft shell crab</span><span class="price">13</span></li>
        <li class="item"><span class="item-name">tiger roll</span><span class="item-desc">shrimp tempura, avocado</span><span class="price">14</span></li>
        <li class="item"><span class="item-name">phoenix roll</span><span class="item-desc">salmon, mango, jalapeño</span><span class="price">15</span></li>
        <li class="item"><span class="item-name">lotus roll</span><span class="item-desc">tuna, yellowtail, cucumber</span><span class="price">16</span></li>
        <li class="item"><span class="item-name">crunch roll</span><span class="item-desc">spicy tuna, tempura flakes</span><span class="price">13</span></li>
        <li class="item"><span class="item-name">ocean roll</span><span class="item-desc">crab, lobster, tobiko</span><span class="price">18</span></li>
        <li class="item"><span class="item-name">sunset roll</span><span class="item-desc">salmon, lemon, avocado</span><span class="price">14</span></li>
      </ul>
    </div>

    <div class="menu-col">
      <ul>
        <li class="item"><span class="item-name">samurai roll</span><span class="item-desc">seared beef, scallion</span><span class="price">16</span></li>
        <li class="item"><span class="item-name">geisha roll</span><span class="item-desc">tuna wrapped in cucumber</span><span class="price">15</span></li>
        <li class="item"><span class="item-name">firecracker roll</span><span class="item-desc">spicy yellowtail, jalapeño</span><span class="price">15</span></li>
        <li class="item"><span class="item-name">golden roll</span><span class="item-desc">shrimp, mango, coconut</span><span class="price">14</span></li>
        <li class="item"><span class="item-name">kyoto roll</span><span class="item-desc">eel, cream cheese</span><span class="price">13</span></li>
        <li class="item"><span class="item-name">fuji roll</span><span class="item-desc">spicy crab, avocado</span><span class="price">13</span></li>
        <li class="item"><span class="item-name">bamboo roll</span><span class="item-desc">asparagus, tuna, salmon</span><span class="price">15</span></li>
        <li class="item"><span class="item-name">lava roll</span><span class="item-desc">baked crab, eel sauce</span><span class="price">16</span></li>
      </ul>
      <h2 class="section-title">traditional maki</h2>
      <ul>
        <li class="item"><span class="item-name">tuna roll</span><span class="item-desc"></span><span class="price">6</span></li>
        <li class="item"><span class="item-name">salmon roll</span><span class="item-desc"></span><span class="price">6</span></li>
        <li class="item"><span class="item-name">yellowtail scallion</span><span class="item-desc"></span><span class="price">7</span></li>
        <li class="item"><span class="item-name">california roll</span><span class="item-desc"></span><span class="price">6</span></li>
        <li class="item"><span class="item-name">eel avocado</span><span class="item-desc"></span><span class="price">8</span></li>
        <li class="item"><span class="item-name">spicy tuna</span><span class="item-desc"></span><span class="price">7</span></li>
        <li class="item"><span class="item-name">salmon skin</span><span class="item-desc"></span><span class="price">6</span></li>
        <li class="item"><span class="item-name">philadelphia roll</span><span class="item-desc"></span><span class="price">7</span></li>
      </ul>
    </div>

    <div class="menu-col">
      <ul>
        <li class="item"><span class="item-name">shrimp tempura roll</span><span class="item-desc"></span><span class="price">9</span></li>
        <li class="item"><span class="item-name">salmon avocado roll</span><span class="item-desc"></span><span class="price">7</span></li>
        <li class="item"><span class="item-name">tuna avocado roll</span><span class="item-desc"></span><span class="price">7</span></li>
      </ul>
      <h2 class="section-title">vegetable maki</h2>
      <ul>
        <li class="item"><span class="item-name">avocado roll</span><span class="item-desc"></span><span class="price">5</span></li>
        <li class="item"><span class="item-name">cucumber roll</span><span class="item-desc"></span><span class="price">4</span></li>
        <li class="item"><span class="item-name">sweet potato</span><span class="item-desc"></span><span class="price">5</span></li>
        <li class="item"><span class="item-name">oshinko roll</span><span class="item-desc"></span><span class="price">4</span></li>
        <li class="item"><span class="item-name">asparagus roll</span><span class="item-desc"></span><span class="price">5</span></li>
        <li class="item"><span class="item-name">shiitake roll</span><span class="item-desc"></span><span class="price">5</span></li>
        <li class="item"><span class="item-name">kanpyo roll</span><span class="item-desc"></span><span class="price">4</span></li>
      </ul>
      <h2 class="section-title">sushi &amp; sashimi</h2>
      <ul class="fish-grid">
        <li class="item"><span class="item-name">tuna</span><span class="item-desc"></span><span class="price">3</span></li>
        <li class="item"><span class="item-name">salmon</span><span class="item-desc"></span><span class="price">3</span></li>
        <li class="item"><span class="item-name">yellowtail</span><span class="item-desc"></span><span class="price">3</span></li>
        <li class="item"><span class="item-name">eel</span><span class="item-desc"></span><span class="price">3</span></li>
        <li class="item"><span class="item-name">shrimp</span><span class="item-desc"></span><span class="price">2</span></li>
        <li class="item"><span class="item-name">squid</span><span class="item-desc"></span><span class="price">2</span></li>
        <li class="item"><span class="item-name">octopus</span><span class="item-desc"></span><span class="price">2</span></li>
        <li class="item"><span class="item-name">mackerel</span><span class="item-desc"></span><span class="price">2</span></li>
        <li class="item"><span class="item-name">scallop</span><span class="item-desc"></span><span class="price">3</span></li>
        <li class="item"><span class="item-name">tamago</span><span class="item-desc"></span><span class="price">2</span></li>
        <li class="item"><span class="item-name">flounder</span><span class="item-desc"></span><span class="price">3</span></li>
        <li class="item"><span class="item-name">salmon roe</span><span class="item-desc"></span><span class="price">4</span></li>
        <li class="item"><span class="item-name">sea urchin</span><span class="item-desc"></span><span class="price">6</span></li>
        <li class="item"><span class="item-name">red snapper</span><span class="item-desc"></span><span class="price">3</span></li>
        <li class="item"><span class="item-name">surf clam</span><span class="item-desc"></span><span class="price">3</span></li>
      </ul>
      <h2 class="section-title">combination</h2>
      <ul style="padding-right:60px">
        <li class="item"><span class="item-name">sushi regular</span><span class="item-desc">eight pieces, tuna roll</span><span class="price">22</span></li>
        <li class="item"><span class="item-name">sushi deluxe</span><span class="item-desc">ten pieces, one roll</span><span class="price">27</span></li>
        <li class="item"><span class="item-name">sashimi regular</span><span class="item-desc">twelve assorted pieces</span><span class="price">25</span></li>
        <li class="item"><span class="item-name">maki combo</span><span class="item-desc">three classic rolls</span><span class="price">17</span></li>
        <li class="item"><span class="item-name">vegetable combo</span><span class="item-desc">three veggie rolls</span><span class="price">14</span></li>
        <li class="item"><span class="item-name">sushi sashimi combo</span><span class="item-desc">for one</span><span class="price">30</span></li>
      </ul>
    </div>
  </div>
  <div class="brand-block brand-block--small">
    <div class="brand-dot"></div>
    <div class="brand-name">Kazeno<br>Sushi Bar</div>
  </div>
  <footer class="bottom-band">
    <p>Please inform your server of any allergies before ordering.</p>
    <p>Consuming raw or undercooked fish may increase health risk.</p>
  </footer>
</section>

</body>
</html>
```